One-Page Flat Design for SEO Company [2 DAYS]

We need a one-page flat design for our SEO company. Our current website is http://www.rankloft.com/. We are looking to completely re-design the site using new flat design techniques.
Below are some examples of the type of style we're going after:
http://quormel.com/
http://tobyrand.co.uk/
https://pentaly.co/
http://milesporter.me/
As you can see- flat, clean, minimal. It is very important you follow this type of style.
For colour scheme, you may use one of the pre-made colour palettes from here:
http://www.vornacle.com/blog/inspiration/24-flat-designs-with-compelling-color-palettes
I've attached a wireframe to be followed.
Hi,

```html
<!DOCTYPE html>
<html lang="en">
<head>
<meta charset="utf-8">
<title>RankLoft – SEO Services</title>
<link href="https://fonts.googleapis.com/css2?family=Open+Sans:wght@400;600;700;800&display=swap" rel="stylesheet">
<style>
:root{
  --orange:#f7941d;
  --orange-dark:#e8780c;
  --ink:#2b2b2b;
  --charcoal:#333333;
  --charcoal-2:#2a2a2a;
  --light:#f1f1f1;
  --text:#444;
  --muted:#777;
  --sky:#3aa8da;
  --teal:#2b86ad;
  --bronze:#5bb4e5;
  --silver:#f39c12;
  --gold:#27ae60;
  --platinum:#e74c3c;
  --white:#fff;
}
*{box-sizing:border-box;margin:0;padding:0}
html,body{width:1200px;height:3448px;overflow:hidden}
body{font-family:"Open Sans",Arial,sans-serif;color:var(--text);background:var(--white);position:relative}
.btn{display:inline-block;font-weight:700;font-size:15px;color:var(--white);background:var(--charcoal-2);padding:10px 24px;border-radius:3px;text-decoration:none}

/* header */
.site-header{height:112px;background:var(--charcoal-2);position:relative}
.brand{position:absolute;left:100px;top:30px;display:flex;align-items:center;gap:12px;color:var(--orange);font-weight:800;font-size:40px;line-height:1}
.brand-dot{width:20px;height:20px;background:var(--orange)}
.main-nav{position:absolute;right:100px;top:0;display:flex;height:112px}
.main-nav a{display:flex;align-items:center;padding:0 22px;color:#ddd;font-size:15px;text-decoration:none}
.main-nav a.active{background:var(--orange);color:var(--white)}

/* hero */
.hero{height:400px;background:linear-gradient(180deg,#fba23a,var(--orange-dark));position:relative;color:var(--white)}
.hero h1{position:absolute;left:100px;top:100px;width:520px;font-size:44px;font-weight:600;line-height:1.2}
.hero p{position:absolute;left:100px;top:225px;width:520px;font-size:15px;line-height:1.6}
.hero-art{position:absolute;right:150px;top:40px;width:380px;height:320px;border-radius:50%;background:radial-gradient(circle,#555 0 35%,#f8a94a 36% 100%);opacity:.9}
.slide-arrow{position:absolute;top:50%;width:28px;height:44px;margin-top:-22px;background:rgba(0,0,0,.45)}
.slide-arrow svg{width:100%;height:100%}
.slide-arrow.left{left:0}.slide-arrow.right{right:0}

/* why */
.why{height:428px;background:var(--light);text-align:center;padding-top:38px}
.section-title{font-size:34px;font-weight:800;color:var(--ink)}
.section-intro{width:960px;margin:14px auto 0;font-size:14px;line-height:1.6;color:var(--muted)}
.feature-row{display:flex;justify-content:center;gap:120px;margin-top:30px}
.feature{width:260px}
.feature-icon{width:96px;height:96px;margin:0 auto;border-radius:50%;background:var(--charcoal-2);border:6px solid var(--orange);display:flex;align-items:center;justify-content:center}
.feature h3{font-size:22px;font-weight:600;color:var(--ink);margin:14px 0 8px}
.feature p{font-size:13px;line-height:1.55;color:var(--muted);margin-bottom:18px}

/* packages */
.packages{height:760px;background:var(--charcoal);text-align:center;padding-top:40px;color:var(--white)}
.packages .section-title{color:var(--white)}
.packages .section-intro{color:#bbb}
.price-grid{display:flex;justify-content:center;gap:12px;margin-top:34px}
.plan{width:215px;background:var(--white);color:var(--text);padding-bottom:26px}
.plan-name{font-size:28px;font-weight:600;color:var(--white);padding:10px 0}
.plan-price{font-size:28px;color:#555;padding:16px 0;border-bottom:1px solid #e2e2e2}
.plan ul{list-style:none;font-size:12px}
.plan li{padding:14px 0;border-bottom:1px solid #eee}
.plan .btn{margin-top:22px;font-weight:600}
.bronze .plan-name,.bronze .btn{background:var(--bronze)}
.silver .plan-name,.silver .btn{background:var(--silver)}
.gold .plan-name,.gold .btn{background:var(--gold)}
.platinum .plan-name,.platinum .btn{background:var(--platinum)}

/* cta */
.cta-band{height:160px;background:var(--sky);color:var(--white);position:relative}
.cta-band p{position:absolute;left:100px;top:48px;width:760px;font-size:20px;line-height:1.5}
.cta-band .btn{position:absolute;right:140px;top:55px;font-size:18px;padding:14px 26px}

/* services */
.services{height:520px;background:var(--teal);text-align:center;padding-top:40px;color:var(--white);position:relative}
.services .section-title{color:var(--ink)}
.services .section-intro{color:#d8eef8}
.services .slide-arrow{background:var(--white);border-radius:50%;width:40px;height:40px;margin-top:10px}
.services .slide-arrow.left{left:20px}.services .slide-arrow.right{right:20px}
.service-row{display:flex;justify-content:center;gap:110px;margin-top:36px}
.service{width:280px}
.service .feature-icon{width:120px;height:120px;border-width:7px}
.service h3{font-size:20px;font-weight:600;color:#1d2a33;margin:16px 0 8px}
.service p{font-size:13px;line-height:1.55;color:#cfe7f2;margin-bottom:18px}

/* contact */
.contact{height:720px;background:var(--white);text-align:center;padding-top:40px}
.contact-line{font-size:19px;color:var(--ink);margin-top:20px}
.contact-form{width:1000px;margin:40px auto 0;display:grid;grid-template-columns:1fr 1fr;gap:20px}
.field{height:60px;border:1px solid #ddd;text-align:left;padding:20px;font-size:12px;color:#999}
.field.message{grid-column:1/3;height:240px}
.send{display:inline-block;margin-top:30px;background:var(--charcoal-2);color:var(--white);width:180px;padding:14px 0;font-weight:700}
.social-links{display:flex;justify-content:center;gap:60px;margin-top:40px;font-weight:700;color:var(--ink);font-size:16px}

/* footer */
.site-footer{height:368px;background:var(--charcoal);color:#ddd;text-align:center;position:relative;padding-top:50px}
.site-footer .brand{position:static;justify-content:center}
.footer-info{margin-top:60px;font-size:20px;line-height:1.6}
.copyright{position:absolute;left:0;right:0;bottom:0;height:50px;line-height:50px;background:var(--charcoal-2);font-size:12px;color:#999}
</style>
</head>
<body>

<header class="site-header">
  <div class="brand"><span class="brand-dot"></span>RankLoft</div>
  <nav class="main-nav">
    <a class="active" href="#">Home</a><a href="#">About Us</a><a href="#">Our Services</a><a href="#">Work</a><a href="#">Team</a><a href="#">Contact</a>
  </nav>
</header>

<section class="hero">
  <h1>Finally, SEO Services that actually work</h1>
  <p>We provide high quality SEO services that are guaranteed to give your rankings a boost. All of our services follow current search guidelines and are updated often for the latest changes.</p>
  <div class="hero-art" role="img" aria-label="Illustration of a large SEO gauge surrounded by search engine badges"></div>
  <span class="slide-arrow left"><svg viewBox="0 0 28 44"><path d="M18 14 10 22l8 8" fill="none" stroke="#fff" stroke-width="3"/></svg></span>
  <span class="slide-arrow right"><svg viewBox="0 0 28 44"><path d="M10 14l8 8-8 8" fill="none" stroke="#fff" stroke-width="3"/></svg></span>
</section>

<section class="why">
  <h2 class="section-title">WHY CHOOSE RANKLOFT</h2>
  <p class="section-intro">Duis gravida vulputate nibh, at semper sapien vulputate non. In nibh nibh, lacinia in vulputate eu, consectetur adipiscing elit. Duis gravida vulputate nibh, at semper sapien vulputate non lacinia.</p>
  <div class="feature-row">
    <div class="feature">
      <div class="feature-icon"><svg width="50" height="50" viewBox="0 0 50 50"><text x="25" y="38" text-anchor="middle" font-family="Open Sans,sans-serif" font-size="38" font-weight="700" fill="#fff">$</text></svg></div>
      <h3>Low Prices</h3>
      <p>Lorem ipsum dolor sit amet, consectetur adipiscing elit. Integer sed magna vel velit dignissim luctus eu in urna. Dapibus egestas turpis.</p>
      <a class="btn" href="#">Read More</a>
    </div>
    <div class="feature">
      <div class="feature-icon"><svg width="50" height="50" viewBox="0 0 50 50"><path d="M8 40 20 26l8 7 14-18" fill="none" stroke="#fff" stroke-width="5"/><path d="M34 12h10v10" fill="none" stroke="#fff" stroke-width="5"/></svg></div>
      <h3>Increased Ranking</h3>
      <p>Lorem ipsum dolor sit amet, consectetur adipiscing elit. Integer sed magna vel velit dignissim luctus eu in urna. Dapibus egestas turpis.</p>
      <a class="btn" href="#">Read More</a>
    </div>
    <div class="feature">
      <div class="feature-icon"><svg width="50" height="50" viewBox="0 0 50 50"><rect x="8" y="30" width="8" height="12" fill="#fff"/><rect x="21" y="22" width="8" height="20" fill="#fff"/><rect x="34" y="12" width="8" height="30" fill="#fff"/></svg></div>
      <h3>High Quality Services</h3>
      <p>Lorem ipsum dolor sit amet, consectetur adipiscing elit. Integer sed magna vel velit dignissim luctus eu in urna. Dapibus egestas turpis.</p>
      <a class="btn" href="#">Read More</a>
    </div>
  </div>
</section>

<section class="packages">
  <h2 class="section-title">RANKLOFT PACKAGES</h2>
  <p class="section-intro">The most effective way to skyrocket your site on search engines is a bundle of high quality backlinks to your website. Our handpicked team of link builders are SEO experts who have helped many clients climb the results. Our services will surely boost your site higher.</p>
  <div class="price-grid">
    <div class="plan bronze"><div class="plan-name">Bronze</div><div class="plan-price">$5.99 /month</div>
      <ul><li>1x PR9 - PR8 Social Bookmarks</li><li>1x PR6 - PR4 2.0 Profile</li><li>1x 1000 Backlinks</li><li>Delivered within 6 days</li><li>Detailed Submission Report</li></ul>
      <a class="btn" href="#">Get Started Now</a></div>
    <div class="plan silver"><div class="plan-name">Silver</div><div class="plan-price">$5.99 /month</div>
      <ul><li>1x PR9 - PR8 Social Bookmarks</li><li>1x PR6 - PR4 2.0 Profile</li><li>1x 1000 Backlinks</li><li>Delivered within 6 days</li><li>Detailed Submission Report</li></ul>
      <a class="btn" href="#">Get Started Now</a></div>
    <div class="plan gold"><div class="plan-name">Gold</div><div class="plan-price">$5.99 /month</div>
      <ul><li>1x PR9 - PR8 Social Bookmarks</li><li>1x PR6 - PR4 2.0 Profile</li><li>1x 1000 Backlinks</li><li>Delivered within 6 days</li><li>Detailed Submission Report</li></ul>
      <a class="btn" href="#">Get Started Now</a></div>
    <div class="plan platinum"><div class="plan-name">Platinum</div><div class="plan-price">$5.99 /month</div>
      <ul><li>1x PR9 - PR8 Social Bookmarks</li><li>1x PR6 - PR4 2.0 Profile</li><li>1x 1000 Backlinks</li><li>Delivered within 6 days</li><li>Detailed Submission Report</li></ul>
      <a class="btn" href="#">Get Started Now</a></div>
  </div>
</section>

<section class="cta-band">
  <p>Lorem ipsum dolor sit amet, consectetur adipiscing elit. Donec scelerisque faucibus risus non iaculis. Fusce a augue ante.</p>
  <a class="btn" href="#">Get Started Now</a>
</section>

<section class="services">
  <h2 class="section-title">INDIVIDUAL SEO SERVICES</h2>
  <p class="section-intro">Maybe you don't need to purchase one of our pre-made SEO packages. No problem. We offer a wide range of individual SEO services for your choosing.</p>
  <span class="slide-arrow left"><svg viewBox="0 0 40 40"><path d="M23 13l-7 7 7 7" fill="none" stroke="#2b86ad" stroke-width="3"/></svg></span>
  <span class="slide-arrow right"><svg viewBox="0 0 40 40"><path d="M17 13l7 7-7 7" fill="none" stroke="#2b86ad" stroke-width="3"/></svg></span>
  <div class="service-row">
    <div class="service">
      <div class="feature-icon"><svg width="60" height="60" viewBox="0 0 60 60"><circle cx="30" cy="30" r="8" fill="#fff"/><circle cx="12" cy="14" r="6" fill="#fff"/><circle cx="48" cy="14" r="6" fill="#fff"/><circle cx="12" cy="46" r="6" fill="#fff"/><circle cx="48" cy="46" r="6" fill="#fff"/><path d="M12 14 30 30 48 14M12 46 30 30 48 46" stroke="#fff" stroke-width="3"/></svg></div>
      <h3>Verified Profile Backlinks</h3>
      <p>Lorem ipsum dolor sit amet, consectetur adipiscing elit. Integer sed magna vel velit dignissim luctus eu in urna.</p>
      <a class="btn" href="#">Read More</a>
    </div>
    <div class="service">
      <div class="feature-icon"><svg width="60" height="60" viewBox="0 0 60 60"><path d="M8 12h44v28H26l-10 10V40H8z" fill="#fff"/></svg></div>
      <h3>Blog Comment Backlinks</h3>
      <p>Lorem ipsum dolor sit amet, consectetur adipiscing elit. Integer sed magna vel velit dignissim luctus eu in urna.</p>
      <a class="btn" href="#">Read More</a>
    </div>
    <div class="service">
      <div class="feature-icon"><svg width="60" height="60" viewBox="0 0 60 60"><circle cx="30" cy="30" r="16" fill="none" stroke="#fff" stroke-width="10" stroke-dasharray="7 5"/><circle cx="30" cy="30" r="7" fill="#fff"/></svg></div>
      <h3>PR4 - PR9 Link Wheels</h3>
      <p>Lorem ipsum dolor sit amet, consectetur adipiscing elit. Integer sed magna vel velit dignissim luctus eu in urna.</p>
      <a class="btn" href="#">Read More</a>
    </div>
  </div>
</section>

<section class="contact">
  <h2 class="section-title">GET IN TOUCH</h2>
  <p class="contact-line">48 Larkspur Row, Fenwick, OR 97042, United States of America. Tel: (555) 014-2290</p>
  <form class="contact-form">
    <div class="field">NAME</div>
    <div class="field">ADDRESS</div>
    <div class="field message">YOUR MESSAGE</div>
  </form>
  <span class="send">SEND</span>
  <div class="social-links"><span>Friendnet</span><span>Chirper</span><span>Circlely</span><span>Worklink</span></div>
</section>

<footer class="site-footer">
  <div class="brand"><span class="brand-dot"></span>RankLoft</div>
  <div class="footer-info">
    <p>Address: 48 Larkspur Row, Fenwick, OR 97042, United States of America.</p>
    <p>Mail: support@rankloft.com, www.rankloft.com</p>
    <p>Phone: (555) 014-2290</p>
  </div>
  <div class="copyright">© 2014 rankloft.com. All rights reserved. Terms of Use</div>
</footer>

</body>
</html>
```